A Real Estate Company Needs a Business Card Design

We need a business card design for a new company based in Boston MA called "Brellmont Real Estate LLC" we are a small company but we like a big corporate look, a simple, sleek, modern and progressive look. we would like the option of having a design that could include the real estate agents personal photo and also a design if the realtor decides not to have a photo. we do not have LOGO at this moment, please use any property look pic corporate with word" Brellmont Real Estate LLC" please see attached file as an example.

```html
<!DOCTYPE html>
<html lang="en">
<head>
<meta charset="utf-8">
<title>Brellmont Real Estate LLC – Business Card</title>
<link href="https://fonts.googleapis.com/css2?family=Ubuntu:wght@400;500;700&display=swap" rel="stylesheet">
<style>
  :root {
    --canvas: #d9d9d9;
    --brand-red: #d4003a;
    --paper: #f1f1ef;
    --charcoal: #2d2d2d;
    --ink: #333333;
    --text-light: #e6e6e6;
    --text-muted: #b5b5b5;
    --white: #ffffff;
  }
  * { box-sizing: border-box; margin: 0; padding: 0; }
  html, body {
    width: 1200px;
    height: 1000px;
    overflow: hidden;
  }
  body {
    background: var(--canvas);
    font-family: "Ubuntu", sans-serif;
    position: relative;
  }
  .card {
    position: absolute;
    left: 220px;
    width: 760px;
    height: 434px;
    box-shadow: 0 6px 18px rgba(0,0,0,0.18);
    overflow: hidden;
  }
  /* Front side */
  .card-front {
    top: 44px;
    background: var(--brand-red);
    display: flex;
    align-items: center;
    justify-content: center;
  }
  .wordmark {
    display: flex;
    align-items: center;
    gap: 16px;
    color: var(--white);
    font-weight: 700;
  }
  .wordmark-square {
    width: 34px;
    height: 34px;
    background: currentColor;
    flex-shrink: 0;
  }
  .wordmark-name {
    display: flex;
    flex-direction: column;
    line-height: 1.05;
  }
  .wordmark-name .primary {
    font-size: 50px;
    letter-spacing: 1px;
  }
  .wordmark-name .secondary {
    font-size: 20px;
    letter-spacing: 1.5px;
    align-self: center;
  }
  /* Back side */
  .card-back {
    top: 522px;
    display: flex;
  }
  .back-brand {
    width: 48%;
    background: var(--paper);
    display: flex;
    align-items: center;
    justify-content: center;
  }
  .back-brand .wordmark { color: var(--ink); gap: 12px; }
  .back-brand .wordmark-square { width: 24px; height: 24px; background: var(--brand-red); }
  .back-brand .wordmark-name .primary { font-size: 36px; }
  .back-brand .wordmark-name .secondary { font-size: 14px; }
  .back-details {
    position: relative;
    flex: 1;
    background: var(--charcoal);
    padding: 78px 40px 0 58px;
    color: var(--text-light);
  }
  .holder-name {
    font-size: 26px;
    font-weight: 700;
    color: var(--text-light);
  }
  .holder-title {
    font-size: 20px;
    color: var(--text-muted);
    margin-top: 2px;
  }
  .contact-list {
    list-style: none;
    margin-top: 34px;
    font-size: 20px;
    line-height: 1.75;
  }
  .contact-list .label { margin-right: 6px; }
  .accent-tab {
    position: absolute;
    right: 0;
    top: 150px;
    width: 12px;
    height: 42px;
    background: var(--brand-red);
  }
</style>
</head>
<body>
  <section class="card card-front" aria-label="Business card front">
    <div class="wordmark">
      <span class="wordmark-square" aria-hidden="true"></span>
      <div class="wordmark-name">
        <span class="primary">BRELLMONT</span>
        <span class="secondary">REAL ESTATE LLC</span>
      </div>
    </div>
  </section>

  <section class="card card-back" aria-label="Business card back">
    <div class="back-brand">
      <div class="wordmark">
        <span class="wordmark-square" aria-hidden="true"></span>
        <div class="wordmark-name">
          <span class="primary">BRELLMONT</span>
          <span class="secondary">REAL ESTATE LLC</span>
        </div>
      </div>
    </div>
    <div class="back-details">
      <p class="holder-name">Cardholder Name</p>
      <p class="holder-title">founder/ceo</p>
      <ul class="contact-list">
        <li><span class="label">a :</span>your street address</li>
        <li><span class="label">p :</span>555 0148 20 73</li>
        <li><span class="label">e :</span>yourmail@brellmont.com</li>
        <li><span class="label">w :</span>www.brellmont.com</li>
      </ul>
      <span class="accent-tab" aria-hidden="true"></span>
    </div>
  </section>
</body>
</html>
```